Picket Sign Advertising For Alaska Tour Company

I would like a relator style picket sign made that I can place by the water near hotels to generate phone calls and website visits. I want to Advertise Our Daily Jet Boat Tours & Jet Ski Tours. This will be a one sided sign. You may be able to see our past brochure and flyer designs and logo. Our FB page is Harlow Summit Excursions and our website is harlowsummitexcursions.com or contact number is 907-518-4463

```html
<!DOCTYPE html>
<html lang="en">
<head>
<meta charset="utf-8">
<title>Harlow Summit Excursions – Jet Ski &amp; Jet Boat Tours</title>
<link rel="stylesheet" href="https://fonts.googleapis.com/css2?family=Anton&family=Montserrat:wght@600;700&display=swap">
<style>
  :root {
    --ink: #000000;
    --water-deep: #1d5a96;
    --water-mid: #3f86c4;
    --water-light: #8cc0e6;
    --sky: #ffffff;
    --ski-red: #d8262c;
    --ski-navy: #1c2340;
    --boat-olive: #7f8f4a;
    --boat-dark: #4c5a34;
    --headline-green: #1e9b3e;
    --headline-yellow: #fff200;
    --headline-red: #e8202a;
    --star-blue: #2ea3e0;
    --star-edge: #2b3990;
    --phone-yellow: #fff200;
    --brand-ink: #ffffff;
    --brand-ring: #c9a96a;
    --cream: #f3ecc8;
    --web-ink: #141414;
  }
  html, body { margin: 0; padding: 0; overflow: hidden; background: #ffffff; }
  .sign {
    position: relative;
    width: 742px;
    height: 1200px;
    overflow: hidden;
    background: var(--ink);
  }
  .hero-water {
    position: absolute;
    left: 0; top: 0;
    width: 742px; height: 562px;
    background: linear-gradient(180deg, var(--sky) 0%, var(--sky) 40%, var(--water-light) 46%, var(--water-mid) 62%, var(--water-deep) 100%);
  }
  .hero-jetski {
    position: absolute;
    left: 52px; top: 112px;
    width: 284px; height: 206px;
    border-radius: 40px 40px 60px 60px;
    background: linear-gradient(160deg, var(--ski-red) 0%, var(--ski-red) 50%, var(--ski-navy) 100%);
  }
  .hero-boat {
    position: absolute;
    left: 368px; top: 44px;
    width: 368px; height: 292px;
    border-radius: 30px 30px 50px 50px;
    background: linear-gradient(180deg, var(--boat-dark) 0%, var(--boat-olive) 60%, #9aa563 100%);
  }
  .headline-badge {
    position: absolute;
    left: 25px; top: 397px;
    width: 692px; height: 264px;
  }
  .headline {
    position: absolute;
    left: 0; top: 416px;
    width: 742px;
    margin: 0;
    text-align: center;
    font-family: "Anton", sans-serif;
    font-weight: 400;
    color: var(--headline-green);
    font-size: 104px;
    line-height: 112px;
  }
  .book-star {
    position: absolute;
    left: 187px; top: 630px;
    width: 374px; height: 262px;
  }
  .book-text {
    position: absolute;
    left: 270px; top: 708px;
    width: 200px;
    text-align: center;
    font-family: "Anton", sans-serif;
    color: var(--headline-red);
    font-size: 58px;
    line-height: 52px;
  }
  .phone {
    position: absolute;
    left: 0; top: 881px;
    width: 742px;
    text-align: center;
    font-family: "Anton", sans-serif;
    color: var(--phone-yellow);
    font-size: 80px;
    line-height: 96px;
    letter-spacing: 2px;
  }
  .brand {
    position: absolute;
    left: 20px; top: 968px;
    display: flex;
    align-items: center;
    gap: 18px;
  }
  .brand-dot {
    width: 130px; height: 130px;
    border-radius: 50%;
    border: 3px solid var(--brand-ring);
    box-sizing: border-box;
  }
  .brand-name {
    font-family: "Montserrat", sans-serif;
    font-weight: 700;
    color: var(--brand-ink);
    font-size: 30px;
    line-height: 38px;
    letter-spacing: 1px;
  }
  .tagline {
    position: absolute;
    left: 24px; top: 1101px;
    width: 540px;
    font-family: "Montserrat", sans-serif;
    font-weight: 600;
    color: #ffffff;
    font-size: 15px;
    letter-spacing: 4.6px;
  }
  .listing {
    position: absolute;
    left: 590px;
    display: flex;
    align-items: center;
    gap: 8px;
    font-family: "Montserrat", sans-serif;
    font-weight: 600;
    color: #ffffff;
    font-size: 20px;
  }
  .listing-one { top: 1004px; }
  .listing-two { top: 1084px; }
  .listing-mark {
    width: 22px; height: 22px;
    border-radius: 50%;
    background: #ffffff;
  }
  .web-band {
    position: absolute;
    left: 0; bottom: 0;
    width: 742px; height: 62px;
    background: var(--cream);
    text-align: center;
    font-family: "Montserrat", sans-serif;
    font-weight: 700;
    color: var(--web-ink);
    font-size: 22px;
    line-height: 62px;
    letter-spacing: 8px;
  }
</style>
</head>
<body>
<main class="sign">
  <div class="hero-water" role="img" aria-label="Photo of open blue lake water under a white sky"></div>
  <div class="hero-jetski" role="img" aria-label="Photo of a red and navy jet ski floating on the water"></div>
  <div class="hero-boat" role="img" aria-label="Photo of a green jet boat with a canvas top and two men standing on its bow"></div>

  <svg class="headline-badge" viewBox="0 0 692 264" aria-hidden="true">
    <rect x="9" y="9" width="674" height="246" rx="62" fill="var(--headline-yellow)" stroke="var(--headline-red)" stroke-width="18"/>
  </svg>
  <h1 class="headline">Jet Ski Tours<br>Jet Boat Tours</h1>

  <svg class="book-star" viewBox="0 0 350 250" preserveAspectRatio="none" aria-hidden="true">
    <polygon fill="var(--star-blue)" stroke="var(--star-edge)" stroke-width="5" stroke-linejoin="round"
      points="175,6 200,72 258,22 245,92 340,88 262,132 338,178 248,172 262,244 200,190 172,246 148,188 82,236 102,168 10,170 88,126 18,78 108,88 98,18 150,70"/>
  </svg>
  <div class="book-text">BOOK<br>Now</div>

  <div class="phone">907-518-4463</div>

  <div class="brand">
    <div class="brand-dot"></div>
    <div class="brand-name">HARLOW SUMMIT<br>EXCURSIONS LLC</div>
  </div>
  <div class="tagline">TAKING YOU WHERE YOU WANT TO GO</div>

  <div class="listing listing-one"><span class="listing-mark"></span>TrekRater</div>
  <div class="listing listing-two"><span class="listing-mark"></span>StayNest</div>

  <div class="web-band">harlowsummitexcursions.com</div>
</main>
</body>
</html>
```